Menu Design Project

Recreate the menu front and back AS CLOSE AS POSSIBLE! Colors matching is important. Categories need to correspond with these pages:

Pages are numbered 1-6 1-3 being left to right when menu open 4 back of 1, 5 back of 2, and 6 is back of 3.

page 1 = starters (include flatbreads under this section),
soups & salads

Page 2 = Wings (marlo holding wings art)
Burgers
Burger toppings

Page 3 = Sandwiches and wraps
entrees

Page 4 = Logo (this will be the front page when folded)
hours of operation
phone #
address
email
Facebook or website URL

Page 5 = Lunch specials mon - fri 11am - 4pm
HH menu and times 4-7 mon - fri 10pm - close daily
Raw consumption quote
18% gratuity added to parties of 8 or more

Page 6 = Desserts
Soft drinks
Draft/bottle beers
$5 glass of wine Cab, Pinot Noir, White Zyn, Chardonnay

We cant get the high res files so we are having to recreate the menu.

Need small changes to menu content as well.

Please see attached files for current menu.

• **Front Side of menu***

MARLO’S JUMBO WINGS

Served with House or Blue Cheese Dressing and Celery

GRILLED OR FRIED

5 pieces ..............................................................................5.45
10 pieces.............................................................................10.45
25 pieces...........................................................................23.95
50 pieces...........................................................................44.95

MARLO’S HOMEMADE SAUCES

Marlo's Wing Sauce
Mild
Medium
Hot
Inferno
Honey Garlic
BBQ
Spicy Mango BBQ
Mango Habenero
Cajun
Jamaican Jerk
Rasberry
Spicy Rasberry
Pineapple Teriyaki
Lemon Pepper
Honey Glazed
Guava Tequila Lime
Garlic Parmesan
Honey Mustard

MARLO’S APPETIZERS

One Dozen Steamers ...............................................8.45
Jalapeńo Crab Nuggets ...........................................6.95
Buffalo Chicken Tenders..........................................6.95
Waffle Fries ..............................................................4.95
Sweet Potato Fries ...................................................5.95
Honey Glazed Sweet Potato Fries...........................6.95
Onion Rings..............................................................5.95
Coconut Shrimp .......................................................7.95
Buffalo Shrimp.............................................................7.95
Mozzarella Sticks...................................................6.45

MARLO’S JUICY HALF POUND HOMEMADE BURGERS

All Burgers Served with Crispy Waffle Fries

CHEESEBURGER

Your Choice of American, Swiss, Provolone or
Cheddar Cheese with Sliced Tomato, Red Onion
and Iceberg Lettuce .......................................8.95

BBQ BURGER

Brushed with Barbecue Sauce and Piled High
with Melted Cheddar Cheese, Crispy Onion
Rings,
Sliced Tomato and Iceberg Lettuce ...............9.25

CAJUN BURGER

Dusted with Cajun Seasoning then Covered
with Blue Cheese Crumbles, Crunchy Bacon,
Iceberg Lettuce, Sliced Tomato, Red Onion and
Ranch Dressing ...............................................9.25

TOPPINGS AND EXTRAS .50 EACH

Blue Cheese Crumbles, Sautéed Mushrooms, Sautéed
Onions, Crunchy Bacon, Blue Cheese Dressing,
House Dressing, Onion Rings, BBQ Sauce, Cajun
Seasoning, Dunmore Seasoning, Red Onion,
Sliced Tomato, Chili, Mango and Jalapeńo Salsa

THE “GIANT MARLO BURGER”.................13.95

One Pound of Fresh Ground Beef
Served with Iceberg Lettuce,
Sliced Tomato, Red Onion,

2847 NORTH HARBIN CREST, WEST PALM BEACH, FLORIDA 33415

561-555-0193 • MARLOSGRILLHUT.EXAMPLE

WARNING: CONSUMPTION OF RAW OR UNDERCOOKED MEAT, SEAFOOD OR POULTRY MAY INCREASE THE RISK OF FOOD-BOURNE ILLNESSES.
ASK YOUR SERVER IF YOU HAVE SPECIFIC DIETARY REQUIREMENTS.

Happy Hour Menu
1/4 lb Hamburger..............2.95
1/4 lb Cheeseburger.................3.45
Hot Dog....................1.95
Mozzarella Sticks........................3.45
Steamed Little Neck Clams........4.95

Lunch Specials............6.45
6 Wings and Fries
Chicken Caesar Salad
Buffalo Chicken Wrap and fries
1/4 lb Hot Dog and fries
Hamburger and fries
Cheeseburger and fries

Domestic Draft..............3.00 Regular 2.50 Happy Hour Pitcher 8.95
Fenner Pale
Glendorfer
Glen Pale
Harlan's Pale

Imported Draft..........3.50 Regular 3.00 Happy Hour Pitcher 9.95
Vostrand
Crag Peak

Domestic Bottles.............3.50 Regular 2.25 Happy Hour
Glendorfer
Glen Pale
Glen Pale Citra
Harlan's Pale
Fenner Pale
Pelstrom Extra

Import Bottles...............4.00
Lumera
Lumera Pale
Brovaard
Brovaard Pale
Sandor
Oscuro Sandor
Tres Halcones
Sulon
Varkov Chill
Ned Porter's
Fennick's

Buckets
Domestic Bucket of 5 12.00
Import Bucket of 5 15.00

WINE............................5.50 4.50 Happy Hour
Cabernet
Merlot
Chardonny
White Zinfendel

**Back Menu Side**

SANDWICHES 1 Side

CRISPY CHICKEN BLT
A Lightly Breaded, Crispy Fried, Fresh Chicken Breast with
Crunchy Bacon, Melted Provolone Cheese, Sliced Tomato,
Iceberg Lettuce and Creamy Ranch Dressing .................8.75

MANGO BBQ GRILLED CHICKEN SANDWICH
A Fresh Chicken Breast Grilled to Perfection and Drizzled with
our House Made Mango BBQ Sauce Piled High with Crispy
Onion Rings, Sliced Tomato and Iceberg Lettuce..............8.75

JAMAICAN JERKED MAHI SANDWICH
Juicy Pieces of Sauteed Mahi Rubbed with Jamaican Jerk
Seasoning and Topped with Spicy Mayonnaise,
Iceberg Lettuce, Sliced Tomato and Red Onion .............9.45

BROILED OR BLACKENED FISH SANDWICH.........................8.75
Broiled or Balckened white fish with lettuce and tomato, served with
tartar sauce.
All Sandwiches and Wraps Served with Crispy Waffle Fries

BUFFALO CHICKEN SUB
Buffalo chicken tossed in your choice of sauce with blue cheese dressing. Topped
with lettuce and tomato on a toasted sub roll.................8.75

CHICKEN PARMESAN SUB
Fried chicken tenders topped with provolone cheese and maranara sauce
on a toasted sub roll...................................................8.75

MARLO’S GIANT 1/4LB ALL BEEF HOT DOG...........................6.95 1 Side
SALADS

BUFFALO CHICKEN SALAD
Plain, Mild, Hot or Extra Hot Crispy Chicken Tenders
Covered with Blue Cheese Crumbles and Ranch Dressing
Served over Romaine Lettuce with Cucumbers, Celery,
Diced Tomato and Scallions .............................................8.95

CLASSIC WEDGE
A Wedge of Iceberg Lettuce Topped with
House Blue Cheese Dressing and Diced Tomato ............5.95

CAESAR SALAD
Marlo’s Homemade Version of the Classic......................4.95

TOSSED SALAD
Romaine Lettuce, Cucumbers, Diced Tomatoes, and
Red Onion Tossed in Ranch Dressing ..............................4.95

ADD ONS
Grilled Chicken .................................................................3.95
Sauteed Mahi....................................................................4.95
Grilled Shrimp...................................................................4.95
Crispy Chicken Tenders.....................................................3.95
Crunchy Bacon ................................................................... .95

SIDES
Waffle Fries .....................................................2.25
Sweet Potato Fries..........................................2.95
Honey Glazed Sweet Potato Fries .................3.65
Onion rings .....................................................2.25
Cole Slaw.........................................................2.25
Black Beans and Rice....................................................2.25
Corn on the Cob .............................................. 2.25
Baked Potato...............................................2.25
Mixed Vegetables..................................................2.25

Soups Cup......3.50 Bowl.........5.50
Soup of the Day
Chili

FLATBREADS
BBQ Chicken.....................................7.95
Buffalo Chicken........................7.95

DRINKS
Zolta........................2.45
Diet Zolta ...............2.45
Vale Breeze.............2.45
Orange Whirl ......................2.45
Canyon Fizz ..........2.45
Lemonade .............2.45
Sweet or Unsweetened Tea ..............2.45
APPLE JUICE.............2.45
ORANGE JUICE ........2.45
CRANBERRY JUICE ..2.45
BOTTLED WATER.....2.45
HOT TEA ..................2.45
COFFEE.....................2.45
ALL KIDS DRINKS ARE
SERVED WITH A CUP
AND LID FOR ..............99

DESSERT
Key Lime Pie...................................4.95
Choclate Layered Cake....................4.95
NY Style Cheesecake.........................................4.95
Warm Apple Cobbler................................................4.95
Pruett's Pie..........................................4.95

MARLO’S DINNERS 2 Side
GRILLED MAHI
Fresh Grilled Mahi, with Your Choice of Any Sauce....14.95
GRILLED or FRIED SHRIMP
Juicy Shrimp Hot Off the Grill, with Your Choice
of any Sauce...................................................................13.95
BROILED or BLACKENED FISH
Tender White Fish Brioled or Blackened and Served with Tartar Sauce................13.95
MARINATED PORK TENDERLOIN
Two Tender Pork Medallions Marinated and served with two sides..............................11.95

WRAPS 1 Side
BUFFALO CHICKEN WRAP
Your choice of mild, hot, or extra hot Crispy Chicken Tenders
with Red Onion, Sliced Tomato, Iceberg Lettuce, Blue Cheese
Crumbles and Ranch Dressing in a Flour Tortilla..............8.75
SOUTHWEST CHICKEN WRAP
Grilled chicken with black beans, rice, sour cream, salsa,cheddar
and jack cheese, with our spicy southwest sauce....................8.75
CHICKEN CAESAR WRAP
Fresh Sliced Grilled Chicken Breast in a Flour Tortilla
with Romaine Lettuce and Caesar Dressing ...................8.75
KEY WEST WRAP
Grilled Chicken tossed in mango habanero souce, Lettuce, Tomato, Onion, and
spicy mayo................................................................8.75
CAJUN SHRIMP WRAP
Tender Shrimp Dusted with Cajun Seasoning in a
Flour Tortilla, lettuce, tomatoe, and onion .....9.45

KIDS MENU........5.95 1 Side
Hamburger
Cheeseburger
Hot Dog
Grilled Cheese
Mac n' Cheese
Chicken Tenders

```html
<!DOCTYPE html>
<html lang="en">
<head>
<meta charset="utf-8">
<title>Marlo’s Menu – Inside Spread</title>
<link rel="stylesheet" href="https://fonts.googleapis.com/css2?family=Luckiest+Guy&family=Open+Sans:ital,wght@0,600;0,700;0,800;1,800&family=Roboto+Condensed:wght@700&display=swap">
<style>
:root{
  --page:#ffffff;
  --paper:#fdf1c4;
  --paper-light:#fff8dc;
  --band:#f7b46a;
  --band-soft:#f9cc8c;
  --band-pale:#fbe0a0;
  --heading:#f15a25;
  --heading-edge:#8c2b0e;
  --heading-glow:#ffe27a;
  --ink:#1d1410;
  --accent:#f05a2b;
  --white:#ffffff;
  --border:#f3c9c0;
}
*{box-sizing:border-box;margin:0;padding:0}
html,body{width:1200px;height:1000px;overflow:hidden;background:var(--page)}
body{position:relative;font-family:"Open Sans",Arial,sans-serif;color:var(--ink)}
.spread{position:absolute;left:8px;top:140px;width:1184px;height:722px;
  background:linear-gradient(180deg,var(--paper-light) 0%,var(--paper) 55%,var(--band-pale) 100%);
  border:1px solid var(--border);overflow:hidden}
.waves{position:absolute;inset:0;width:100%;height:100%}
.abs{position:absolute}
.heading{font-family:"Luckiest Guy","Arial Narrow",sans-serif;font-weight:400;color:var(--heading);
  -webkit-text-stroke:1px var(--heading-edge);text-shadow:2px 2px 0 var(--heading-glow);
  letter-spacing:.5px;line-height:1;text-align:center;white-space:nowrap}
.h-lg{font-size:28px}
.h-sm{font-size:21px;line-height:.95}
.h-sm .big{font-size:25px}
.note{font-size:8.6px;font-weight:800;font-style:italic;white-space:nowrap}
.col-left{font-size:8.4px;line-height:11.5px;font-weight:600;width:318px;left:44px}
.col-left .desc>div{white-space:nowrap}
.name{font-weight:800;text-transform:uppercase;white-space:nowrap}
.row{display:flex;align-items:baseline;white-space:nowrap}
.lead{flex:1;border-bottom:1.5px dotted var(--ink);margin:0 3px;transform:translateY(-2px);min-width:6px}
.cond{font-family:"Roboto Condensed","Arial Narrow",sans-serif;font-weight:700}
.col-mid{left:432px;width:296px;font-size:11px;line-height:12.4px}
.col-mid div{white-space:nowrap}
.addons .row{padding-left:4px}
.sides{font-size:11px;line-height:11.9px}
.indent1{padding-left:10px}
.indent2{padding-left:20px}
.drinks{font-size:9.6px;line-height:11.2px;text-transform:uppercase}
.desserts{font-size:10.8px;line-height:11.7px}
.flatbreads{font-size:10.8px;line-height:12px}
.kids{font-size:11px;line-height:12.4px;display:flex;gap:30px}
.hotdog{left:42px;top:618px;width:318px;height:62px;background:var(--accent);color:var(--white);display:flex;align-items:center}
.hotdog .title{font-family:"Luckiest Guy","Arial Narrow",sans-serif;font-size:16px;line-height:15px;text-align:center;width:150px;margin-left:6px;letter-spacing:.5px;white-space:nowrap}
.hotdog .side{margin-left:18px;text-align:center}
.hotdog .side i{display:block;font-size:11.5px;font-weight:800}
.hotdog .side b{display:block;font-family:"Luckiest Guy","Arial Narrow",sans-serif;font-size:21px;font-weight:400;margin-top:2px}
.mascot{left:985px;top:398px;width:199px;height:324px;
  background:linear-gradient(160deg,#f8d34a 0%,#f07a2e 40%,#8b5a3a 65%,#2f7fc1 100%);border-radius:40px 0 0 0;opacity:.9}
</style>
</head>
<body>
<div class="spread">
  <svg class="waves" viewBox="0 0 1184 722" preserveAspectRatio="none" aria-hidden="true">
    <path d="M0 300 C250 260 400 420 700 360 S1050 250 1184 300 L1184 722 L0 722 Z" fill="var(--band-pale)" opacity=".8"/>
    <path d="M0 420 C200 360 420 470 640 420 S980 330 1184 380 L1184 470 C960 420 800 520 600 500 S200 440 0 500 Z" fill="var(--band)" opacity=".75"/>
    <path d="M0 520 C260 470 420 600 700 540 S1000 470 1184 500 L1184 560 C980 540 820 630 620 610 S220 560 0 600 Z" fill="var(--band-soft)" opacity=".8"/>
    <path d="M0 640 C300 590 500 700 760 650 S1050 600 1184 630 L1184 722 L0 722 Z" fill="var(--band)" opacity=".45"/>
    <circle cx="580" cy="20" r="30" fill="var(--heading-glow)" opacity=".7"/>
    <circle cx="1100" cy="90" r="60" fill="none" stroke="var(--heading-glow)" stroke-width="2" opacity=".6"/>
    <circle cx="40" cy="40" r="26" fill="none" stroke="var(--heading-glow)" stroke-width="2" opacity=".6"/>
  </svg>

  <!-- Left column: sandwiches -->
  <div class="abs heading h-lg" style="left:42px;top:30px;width:320px">MARLO’S SANDWICHES</div>
  <div class="abs note" style="left:44px;top:64px">All Sandwiches and Wraps Served with Crispy Waffle Fries</div>

  <div class="abs col-left" style="top:83px">
    <div class="name">Crispy Chicken BLT</div>
    <div class="desc"><div>A Lightly Breaded, Crispy Fried, Fresh Chicken Breast with</div><div>Crunchy Bacon, Melted Provolone Cheese, Sliced Tomato,</div></div>
    <div class="row">Iceberg Lettuce and Creamy Ranch Dressing<span class="lead"></span>8.75</div>
  </div>
  <div class="abs col-left" style="top:135px">
    <div class="name">Mango BBQ Grilled Chicken Sandwich</div>
    <div class="desc"><div>A Fresh Chicken Breast Grilled to Perfection and Drizzled</div><div>with our House Made Mango BBQ Sauce Piled High with Crispy</div></div>
    <div class="row">Onion Rings, Sliced Tomato and Iceberg Lettuce<span class="lead"></span>8.75</div>
  </div>
  <div class="abs col-left" style="top:186px">
    <div class="name">Jamaican Jerked Mahi Sandwich</div>
    <div class="desc"><div>Juicy Pieces of Sauteed Mahi Rubbed with Jamaican Jerk Seasoning</div><div>and Topped with Spicy Mayonnaise, Iceberg Lettuce,</div><div>Sliced Tomato and Red Onion ................... 9.45</div></div>
  </div>
  <div class="abs col-left" style="top:238px">
    <div class="name">Broiled or Blackened Fish Sandwich</div>
    <div class="desc"><div>Broiled or Balckened white fish with lettuce</div></div>
    <div class="row">and tomato, served with tartar sauce<span class="lead"></span>8.75</div>
  </div>
  <div class="abs col-left" style="top:278px">
    <div class="name">Buffalo Chicken Sub</div>
    <div class="desc"><div>Buffalo chicken tossed in your choice of sauce with blue cheese dressing.</div></div>
    <div class="row">Topped with lettuce and tomato on a toasted sub roll<span class="lead"></span>8.75</div>
  </div>
  <div class="abs col-left" style="top:318px">
    <div class="name">Chicken Parmesan Sub</div>
    <div class="desc"><div>Fried chicken tenders topped with provolone cheese</div></div>
    <div class="row">and maranara sauce on a toasted sub roll<span class="lead"></span>8.75</div>
  </div>

  <!-- Left column: wraps -->
  <div class="abs heading h-lg" style="left:42px;top:369px;width:320px">MARLO’S WRAPS</div>
  <div class="abs col-left" style="top:400px">
    <div class="name">Buffalo Chicken Wrap</div>
    <div class="desc"><div>Your choice of mild, hot, or extra hot Crispy Chicken Tenders</div><div>with Red Onion, Sliced Tomato, Iceberg Lettuce, Blue Cheese Crumbles</div></div>
    <div class="row">and Ranch Dressing in a Flour Tortilla<span class="lead"></span>8.75</div>
  </div>
  <div class="abs col-left" style="top:452px">
    <div class="name">Southwest Chicken Wrap</div>
    <div class="desc"><div>Grilled chicken with black beans, rice, sour cream, salsa,</div></div>
    <div class="row">cheddar and jack cheese, with our spicy southwest sauce<span class="lead"></span>8.75</div>
  </div>
  <div class="abs col-left" style="top:491px">
    <div class="name">Chicken Caesar Wrap</div>
    <div class="desc"><div>Fresh Sliced Grilled Chicken Breast in a Flour Tortilla</div></div>
    <div class="row">with Romaine Lettuce and Caesar Dressing<span class="lead"></span>8.75</div>
  </div>
  <div class="abs col-left" style="top:531px">
    <div class="name">Key West Wrap</div>
    <div class="desc"><div>Grilled Chicken tossed in mango habanero souce, Lettuce,</div></div>
    <div class="row">Tomato, Onion, and spicy mayo<span class="lead"></span>8.75</div>
  </div>
  <div class="abs col-left" style="top:571px">
    <div class="name">Cajun Shrimp Wrap</div>
    <div class="desc"><div>Tender Shrimp Dusted with Cajun Seasoning in a Flour Tortilla,</div></div>
    <div class="row">lettuce, tomatoe, and onion<span class="lead"></span>9.45</div>
  </div>

  <div class="abs hotdog">
    <div class="title">MARLO’S GIANT<br>1/4 LB ALL BEEF<br>HOT DOG</div>
    <div class="side"><i>Served with a Side</i><b>$6.95</b></div>
  </div>

  <!-- Middle column: salads -->
  <div class="abs heading h-lg" style="left:432px;top:30px;width:296px">MARLO’S SALADS</div>
  <div class="abs col-mid cond" style="top:62px">
    <div>BUFFALO CHICKEN SALAD</div>
    <div>Plain, Mild, Hot or Extra Hot Crispy Chicken Tenders</div>
    <div>Covered with Blue Cheese Crumbles and Ranch Dressing</div>
    <div>Served over Romaine Lettuce with Cucumbers, Celery,</div>
    <div class="row">Diced Tomato and Scallions<span class="lead"></span>8.95</div>
  </div>
  <div class="abs col-mid cond" style="top:140px">
    <div>CLASSIC WEDGE</div>
    <div>A Wedge of Iceberg Lettuce Topped with</div>
    <div class="row">House Blue Cheese Dressing and Diced Tomato<span class="lead"></span>5.95</div>
  </div>
  <div class="abs col-mid cond" style="top:178px">
    <div>CAESAR SALAD</div>
    <div class="row">Marlo’s Homemade Version of the Classic<span class="lead"></span>4.95</div>
  </div>
  <div class="abs col-mid cond" style="top:214px">
    <div>TOSSED SALAD</div>
    <div>Romaine Lettuce, Cucumbers, Diced Tomatoes, and</div>
    <div class="row">Red Onion Tossed in Ranch Dressing<span class="lead"></span>4.95</div>
  </div>
  <div class="abs col-mid cond addons" style="top:260px">
    <div>ADD ONS</div>
    <div class="row">Grilled Chicken<span class="lead"></span>3.95</div>
    <div class="row">Sauteed Mahi<span class="lead"></span>4.95</div>
    <div class="row">Grilled Shrimp<span class="lead"></span>4.95</div>
    <div class="row">Crispy Chicken Tenders<span class="lead"></span>3.95</div>
    <div class="row">Crunchy Bacon<span class="lead"></span>.95</div>
  </div>

  <!-- Middle column: dinners -->
  <div class="abs heading h-lg" style="left:432px;top:351px;width:296px">MARLO’S SALADS</div>
  <div class="abs note" style="left:434px;top:379px">All Dinners Served with Two Sides</div>
  <div class="abs col-mid cond" style="top:402px">
    <div>GRILLED MAHI</div>
    <div class="row">Fresh Grilled Mahi, with Your Choice of Any Sauce<span class="lead"></span>14.95</div>
  </div>
  <div class="abs col-mid cond" style="top:437px">
    <div>GRILLED or FRIED SHRIMP</div>
    <div>Juicy Shrimp Hot Off the Grill,</div>
    <div class="row">with Your Choice of any sauce<span class="lead"></span>13.95</div>
  </div>
  <div class="abs col-mid cond" style="top:483px">
    <div>BROILED or BLACKENED FISH</div>
    <div>Tender White Fish Brioled or Blackened</div>
    <div class="row">and Served with Tartar Sauce<span class="lead"></span>13.95</div>
  </div>
  <div class="abs col-mid cond" style="top:531px">
    <div>MARINATED PORK TENDERLOIN</div>
    <div>Two Tender Pork Medallions Marinated</div>
    <div class="row">and served with two sides<span class="lead"></span>11.95</div>
  </div>

  <!-- Middle column: kids -->
  <div class="abs heading h-lg" style="left:432px;top:595px;width:296px">MARLO’S KIDS MENU</div>
  <div class="abs note" style="left:437px;top:625px">All Served with a Side</div>
  <div class="abs kids cond" style="left:437px;top:646px">
    <div>Hamburger<br>Cheeseburger<br>Hot Dog</div>
    <div>Grilled Cheese<br>Mac n' Cheese<br>Chicken Tenders</div>
  </div>

  <!-- Right column: sides -->
  <div class="abs heading h-lg" style="left:826px;top:28px;width:295px">MARLO’S SIDES</div>
  <div class="abs sides cond" style="left:827px;top:67px;width:295px">
    <div class="row">Waffle Fries<span class="lead"></span>2.25</div>
    <div class="row">Sweet Potato Fries<span class="lead"></span>2.95</div>
    <div class="row">Honey Glazed Sweet Potato Fries<span class="lead"></span>3.65</div>
    <div class="row">Onion Rings<span class="lead"></span>2.25</div>
    <div class="row">Cole Slaw<span class="lead"></span>2.25</div>
    <div class="row">Black Beans and Rice<span class="lead"></span>2.25</div>
    <div class="row">Corn on the Cob<span class="lead"></span>2.25</div>
    <div class="row">Baked Potato<span class="lead"></span>2.25</div>
    <div class="row">Mixed Vegetables<span class="lead"></span>2.25</div>
    <div>Soups</div>
    <div class="indent1">Soup of the Day</div>
    <div class="indent1">Chili</div>
    <div class="row indent2">Cup<span class="lead"></span>3.50</div>
    <div class="row indent2">Bowl<span class="lead"></span>5.50</div>
  </div>

  <div class="mascot abs" role="img" aria-label="Illustration of the Marlo’s mascot in sunglasses and a tropical shirt holding a drink beside a surfboard"></div>

  <!-- Right column: drinks -->
  <div class="abs heading h-sm" style="left:826px;top:257px;width:140px">MARLO’S<br>DRINKS</div>
  <div class="abs drinks cond" style="left:827px;top:307px;width:132px">
    <div class="row">Zolta<span class="lead"></span>2.45</div>
    <div class="row">Diet Zolta<span class="lead"></span>2.45</div>
    <div class="row">Vale Breeze<span class="lead"></span>2.45</div>
    <div class="row">Orange Whirl<span class="lead"></span>2.45</div>
    <div class="row">Canyon Fizz<span class="lead"></span>2.45</div>
    <div class="row">Lemonade<span class="lead"></span>2.45</div>
    <div>Sweet or</div>
    <div class="row">Unsweetened Tea<span class="lead"></span>2.45</div>
    <div class="row">Apple Juice<span class="lead"></span>2.45</div>
    <div class="row">Orange Juice<span class="lead"></span>2.45</div>
    <div class="row">Cranberry Juice<span class="lead"></span>2.45</div>
    <div class="row">Bottled Water<span class="lead"></span>2.45</div>
    <div>Hot Drinks</div>
    <div class="row">Hot Tea<span class="lead"></span>2.45</div>
    <div class="row">Coffee<span class="lead"></span>2.45</div>
    <div>Kids Drinks</div>
    <div>All Kids Drinks Are</div>
    <div>Served With A Cup</div>
    <div class="row">And Lid For<span class="lead"></span>.99</div>
  </div>

  <!-- Right column: desserts -->
  <div class="abs heading h-sm" style="left:1015px;top:256px;width:175px">MARLO’S<br><span class="big">DESSERTS</span></div>
  <div class="abs desserts cond" style="left:1002px;top:301px;width:158px">
    <div class="row">Key Lime Pie<span class="lead"></span>4.95</div>
    <div>Chocolate</div>
    <div class="row">Layered Cake<span class="lead"></span>4.95</div>
    <div>NY Style</div>
    <div class="row">Cheesecake<span class="lead"></span>4.95</div>
    <div>Warm Apple</div>
    <div class="row">Cobbler<span class="lead"></span>4.95</div>
    <div class="row">Pruett's Pie<span class="lead"></span>4.95</div>
  </div>

  <!-- Right column: flatbreads -->
  <div class="abs heading h-sm" style="left:826px;top:546px;width:180px">MARLO’S<br><span class="big">FLATBREADS</span></div>
  <div class="abs flatbreads cond" style="left:840px;top:593px;width:126px">
    <div class="row">BBQ Chicken<span class="lead"></span>7.95</div>
    <div class="row">Buffalo Chicken<span class="lead"></span>7.95</div>
  </div>
</div>
</body>
</html>
```